Dorral Fitness fitness and wellness for 50+ and youth

We are a fitness company that caters to 50+ wellness and youth conditioning. Our motto is "We make fitness fun". We offer online wellness programs that include bootcamp style workouts as well as nutrition information/guidance. We would like a design that integrates our logo as well as bring attention to the FUN aspect of being healthy.

Target Market(s)

50+ and parents of teens & tweens

Industry/Entity Type

Fitness

Requirements
Must have
• Topic boxes
Nice to have
• Semi transparent grey or black header with logo integrated

```html
<!DOCTYPE html>
<html lang="en">
<head>
<meta charset="utf-8">
<title>Dorral Fitness</title>
<link href="https://fonts.googleapis.com/css2?family=Open+Sans:wght@400;600;700;800&family=Oswald:wght@500;600&display=swap" rel="stylesheet">
<style>
:root{
  --green:#2dbd1b;
  --green-dark:#1f9610;
  --green-light:#5fe04a;
  --ink:#111213;
  --text:#4b4b4b;
  --muted:#7a7a7a;
  --grey-box:#cfcfcf;
  --white:#ffffff;
}
*{margin:0;padding:0;box-sizing:border-box}
html,body{width:744px;height:1200px;overflow:hidden}
body{background:var(--white);font-family:"Open Sans",Arial,sans-serif;color:var(--text);position:relative}
.site-header{position:absolute;left:0;top:0;width:744px;height:70px;background:linear-gradient(#1c1d1e,var(--ink))}
.brand{position:absolute;left:34px;top:20px;display:flex;align-items:center;gap:9px}
.brand-dot{width:26px;height:26px;border-radius:50%;background:var(--green)}
.brand-name{font-family:"Open Sans",sans-serif;font-weight:700;font-size:22px;color:var(--white);letter-spacing:.2px}
.main-nav{position:absolute;left:0;top:70px;width:744px;height:26px;background:linear-gradient(var(--green-light),var(--green));display:flex;padding-left:114px}
.main-nav a{font-size:9px;font-weight:700;color:var(--white);text-decoration:none;line-height:26px;padding:0 11px;letter-spacing:.3px}
.main-nav a.active{background:var(--green-dark)}
.hero{position:absolute;left:0;top:96px;width:744px;height:282px;background:linear-gradient(100deg,#6d6f72 0%,#a7a9ab 35%,#d6d7d8 60%,#8f9193 100%)}
.hero-caption{position:absolute;left:50px;top:96px;background:rgba(0,0,0,.35);padding:8px 12px}
.hero-title{font-family:"Oswald",sans-serif;font-weight:600;font-size:25px;color:var(--white);letter-spacing:.5px}
.hero-sub{font-family:"Oswald",sans-serif;font-weight:500;font-size:11px;color:var(--green-light);letter-spacing:1px}
.hero-dots{position:absolute;left:355px;bottom:10px;display:flex;gap:6px}
.hero-dots span{width:7px;height:7px;border-radius:50%;background:#bbb}
.hero-dots span.on{background:var(--white)}
.welcome{position:absolute;left:0;top:408px;width:744px;text-align:center}
.welcome h1{font-family:"Open Sans",sans-serif;font-weight:700;font-size:18px;color:#333;letter-spacing:.3px}
.welcome p{width:600px;margin:10px auto 0;font-size:9.5px;line-height:15px;color:var(--muted)}
.topics{position:absolute;left:119px;top:540px;display:flex;gap:27px}
.topic{width:117px;height:150px;background:var(--grey-box);text-align:center;padding-top:14px;color:#555}
.topic.featured{background:var(--green);color:var(--white)}
.topic svg{width:30px;height:30px}
.topic h3{font-size:11px;font-weight:600;margin-top:8px}
.topic p{font-size:8px;line-height:12px;padding:6px 10px 0}
.btn{display:inline-block;font-size:7.5px;font-weight:700;padding:4px 8px;background:#444;color:var(--white);text-decoration:none;margin-top:8px}
.topic .btn{background:#e9e9e9;color:#333}
.features{position:absolute;left:119px;top:742px;display:flex;gap:25px}
.feature{width:160px}
.feature-photo{height:80px}
.feature h3{font-size:10.5px;font-weight:800;color:#333;margin-top:8px}
.feature p{font-size:8px;line-height:12px;color:var(--muted);margin-top:4px}
.feature .btn{background:var(--green);margin-top:6px}
.video-band{position:absolute;left:0;top:913px;width:744px;height:202px;background:linear-gradient(var(--green-light),var(--green))}
.video-band h2{font-family:"Open Sans",sans-serif;font-weight:700;font-size:18px;color:var(--white);text-align:center;margin-top:28px}
.videos{position:absolute;left:119px;top:62px;display:flex;gap:6px}
.video{width:124px;color:var(--white)}
.video-thumb{height:66px;position:relative;display:flex;align-items:center;justify-content:center}
.video h4{font-size:8.5px;font-weight:700;margin-top:6px}
.video p{font-size:7.5px;line-height:11px;margin-top:2px}
.site-footer{position:absolute;left:0;top:1145px;width:744px;height:55px;background:var(--ink)}
.footer-nav{position:absolute;left:48px;top:14px;display:flex;gap:5px;font-size:8.5px;font-weight:600;color:var(--white)}
.copyright{position:absolute;left:48px;top:32px;font-size:7.5px;color:#888}
.social{position:absolute;right:58px;top:16px;display:flex;gap:8px}
.social span{width:10px;height:10px;border-radius:50%;background:var(--white)}
</style>
</head>
<body>

<header class="site-header">
  <div class="brand"><span class="brand-dot"></span><span class="brand-name">Dorral Fitness</span></div>
</header>

<nav class="main-nav">
  <a class="active">HOME</a><a>VIDEO TIPS</a><a>GALLERY</a><a>ARCHIVES</a><a>UPCOMING EVENTS</a><a>LINKS</a><a>CONTACT US</a>
</nav>

<section class="hero" role="img" aria-label="Photo of a woman training with dumbbells and a coach in a gym">
  <div class="hero-caption">
    <div class="hero-title">WE MAKE FITNESS FUN</div>
    <div class="hero-sub">SED MATTIS MASSA CONVALLIS</div>
  </div>
  <div class="hero-dots"><span></span><span class="on"></span><span></span></div>
</section>

<section class="welcome">
  <h1>WELCOME TO DORRAL FITNESS MAINPAGE</h1>
  <p>Dorral Fitness brings bootcamp style workouts, simple nutrition guidance and friendly coaching to adults over fifty and to busy teens and tweens. Every session is built to lift energy, build strength and keep you smiling while you move.</p>
  <p>Join our online wellness program from home, follow weekly video tips and meet us at upcoming events across town.</p>
</section>

<section class="topics">
  <div class="topic featured">
    <svg viewBox="0 0 30 30"><path d="M17 2 6 17h8l-2 11 12-16h-8z" fill="#fff"/></svg>
    <h3>Bootcamp Style</h3>
    <p>Short fun sessions that build strength and stamina at any age.</p>
    <a class="btn">Read more</a>
  </div>
  <div class="topic">
    <svg viewBox="0 0 30 30"><g fill="#fff"><rect x="2" y="10" width="5" height="10"/><rect x="23" y="10" width="5" height="10"/><rect x="7" y="8" width="3" height="14"/><rect x="20" y="8" width="3" height="14"/><rect x="10" y="13.5" width="10" height="3"/></g></svg>
    <h3>Workouts</h3>
    <p>Guided routines for joints, balance, speed and everyday power.</p>
    <a class="btn">Read more</a>
  </div>
  <div class="topic">
    <svg viewBox="0 0 30 30"><circle cx="15" cy="17" r="10" fill="#fff"/><path d="M15 7c1-4 4-5 6-5-1 3-3 5-6 5z" fill="#fff"/></svg>
    <h3>Nutrition Information</h3>
    <p>Easy meal ideas and smart snacks that keep energy steady.</p>
    <a class="btn">Read more</a>
  </div>
  <div class="topic">
    <svg viewBox="0 0 30 30"><circle cx="15" cy="15" r="13" fill="#fff"/><path d="m9 15 4 4 8-8" stroke="#cfcfcf" stroke-width="3" fill="none"/></svg>
    <h3>Guidance</h3>
    <p>Personal coaching that helps families set goals and stay motivated.</p>
    <a class="btn">Read more</a>
  </div>
</section>

<section class="features">
  <div class="feature">
    <div class="feature-photo" role="img" aria-label="Photo of smiling trainers in green shirts" style="background:linear-gradient(135deg,#7ccf5a,#d9c7b0)"></div>
    <h3>WHY CHOOSE US</h3>
    <p>Friendly coaches, small groups and plans shaped around your goals and pace.</p>
    <a class="btn">READ MORE</a>
  </div>
  <div class="feature">
    <div class="feature-photo" role="img" aria-label="Photo of a healthy meal with vegetables" style="background:linear-gradient(135deg,#c9b08a,#6e8f45)"></div>
    <h3>ONLINE WELLNESS PROGRAM</h3>
    <p>Train anywhere with live classes, recorded sessions and weekly check-ins from coaches.</p>
    <a class="btn">READ MORE</a>
  </div>
  <div class="feature">
    <div class="feature-photo" role="img" aria-label="Photo of a woman stretching outdoors at sunset" style="background:linear-gradient(135deg,#f0c24a,#7da83c)"></div>
    <h3>UPCOMING EVENTS</h3>
    <p>Park bootcamps, family fun runs and wellness talks are coming this season.</p>
    <a class="btn">READ MORE</a>
  </div>
</section>

<section class="video-band">
  <h2>LATEST VIDEO TIPS</h2>
  <div class="videos">
    <div class="video">
      <div class="video-thumb" role="img" aria-label="Video still of a gym workout" style="background:linear-gradient(135deg,#555,#999)"><svg width="22" height="22" viewBox="0 0 22 22"><circle cx="11" cy="11" r="10" fill="rgba(0,0,0,.5)"/><path d="m9 7 6 4-6 4z" fill="#fff"/></svg></div>
      <h4>Quick morning stretch</h4>
      <p>Ten minutes to wake up joints and muscles.</p>
    </div>
    <div class="video">
      <div class="video-thumb" role="img" aria-label="Video still of a trainer coaching a client" style="background:linear-gradient(135deg,#8a6f5a,#c8b7a6)"><svg width="22" height="22" viewBox="0 0 22 22"><circle cx="11" cy="11" r="10" fill="rgba(0,0,0,.5)"/><path d="m9 7 6 4-6 4z" fill="#fff"/></svg></div>
      <h4>Core for beginners</h4>
      <p>Gentle moves to build a stronger center.</p>
    </div>
    <div class="video">
      <div class="video-thumb" role="img" aria-label="Video still of fresh salad ingredients" style="background:linear-gradient(135deg,#6fae3d,#e3d9b8)"><svg width="22" height="22" viewBox="0 0 22 22"><circle cx="11" cy="11" r="10" fill="rgba(0,0,0,.5)"/><path d="m9 7 6 4-6 4z" fill="#fff"/></svg></div>
      <h4>Smart snack ideas</h4>
      <p>Simple bites that fuel a busy afternoon.</p>
    </div>
    <div class="video">
      <div class="video-thumb" role="img" aria-label="Video still of a group class exercising" style="background:linear-gradient(135deg,#4d6a8a,#b7c2cc)"><svg width="22" height="22" viewBox="0 0 22 22"><circle cx="11" cy="11" r="10" fill="rgba(0,0,0,.5)"/><path d="m9 7 6 4-6 4z" fill="#fff"/></svg></div>
      <h4>Family bootcamp fun</h4>
      <p>Games and drills the whole house enjoys.</p>
    </div>
  </div>
</section>

<footer class="site-footer">
  <div class="footer-nav"><span>HOME</span><span>|</span><span>ARCHIVES</span><span>|</span><span>VIDEO TIPS</span><span>|</span><span>GALLERY</span><span>|</span><span>UPCOMING EVENTS</span><span>|</span><span>CONTACT US</span></div>
  <div class="copyright">© 2024 Dorral Fitness. All rights reserved.</div>
  <div class="social"><span></span><span></span><span></span><span></span></div>
</footer>

</body>
</html>
```